Brenwick Structures Construction Company Seeking Modern Website

We are a small construction company wanting to create a web presence. We don't have much in the way of current content but will get photos as they come in. Attached is a picture of our business card.
The pages we would like on the menu are:
Home
Portfolio
Product Specs
Testimonials
Our Process
Contact
Some designs we like are:
http://www.tovandrafters.example/
http://www.qrkframes.example/
http://harnestshed.example/
http://pellowbarns.example/
Not much requirements other than that so feel free to be creative!
Target Market(s)
Construction
Commercial and Residential Buildings
Industry/Entity Type
Construction Company
Number of Pages Required
5+ page

```html
<!DOCTYPE html>
<html lang="en">
<head>
<meta charset="utf-8">
<title>Brenwick Structures</title>
<link href="https://fonts.googleapis.com/css2?family=Great+Vibes&family=Lato:wght@400;700;900&family=Raleway:ital,wght@0,400;0,600;0,700;1,400&display=swap" rel="stylesheet">
<style>
:root{
  --navy:#1d2a44;
  --red:#d20a0a;
  --blue:#2e9fd3;
  --blue-dark:#2389bd;
  --blue-bar:#33a6dc;
  --accent:#3a9ad0;
  --ink:#333;
  --text:#4a4a4a;
  --paper:#f3f3f3;
  --band:#e1e1e1;
  --card-head:#5a5a5a;
}
*{margin:0;padding:0;box-sizing:border-box}
html,body{width:794px;height:1200px;overflow:hidden}
body{position:relative;background:var(--paper);font-family:"Raleway",sans-serif;color:var(--text)}
.abs{position:absolute}
.script{font-family:"Great Vibes",cursive;font-weight:400}

/* hero */
.hero{left:0;top:0;width:794px;height:383px;background:linear-gradient(180deg,#4f79b6 0%,#8fb0d8 25%,#b2642e 50%,#c9773a 62%,#6a8a3a 82%,#4d6d2d 100%)}
.topbar{left:0;top:0;width:794px;height:22px;background:rgba(22,34,60,.85)}
.topbar .social{left:530px;top:5px;display:flex;gap:6px}
.topbar .social span{width:12px;height:12px;border-radius:50%;background:var(--red)}
.topbar .phone{left:594px;top:3px;color:#fff;font:700 11px "Lato",sans-serif;display:flex;align-items:center;gap:6px}
.header{left:0;top:22px;width:794px;height:50px;background:rgba(240,240,244,.88)}
.logo{left:104px;top:15px;width:192px;display:flex;align-items:center;gap:6px;font:900 16px "Lato",sans-serif;color:#1166c4;white-space:nowrap}
.logo i{flex:none;width:11px;height:11px;background:var(--red);border-radius:50%}
.nav{left:304px;top:0;height:48px;display:flex;list-style:none}
.nav li{height:48px;display:flex;align-items:center;padding:0 13px;font:700 8px "Lato",sans-serif;color:#222;border-right:1px solid #c8c8cc}
.nav li.active{background:var(--red);color:#fff;padding:0 12px;border:0}
.arrow{top:204px;width:20px;height:20px;border-radius:50%;background:rgba(230,230,230,.85)}
.caption{left:0;top:330px;width:794px;height:53px;background:linear-gradient(180deg,rgba(0,0,0,0),rgba(0,0,0,.35));color:#fff;font-size:26px;text-align:center;line-height:48px}

/* section headings */
.heading{width:794px;left:0;text-align:center;font-size:22px;color:#222}
.heading em{font-style:normal;color:var(--accent)}
.rule{left:240px;width:314px;height:1px;background:#cfcfcf}
.rule::after{content:"";position:absolute;left:147px;top:-2px;width:19px;height:5px;border-radius:3px;background:var(--red)}
.intro{left:112px;top:451px;width:570px;font-size:8.2px;line-height:15.2px;text-align:center}

/* feature cards */
.band{left:0;top:578px;width:794px;height:152px;background:var(--band)}
.card{top:553px;width:179px;height:147px;background:#fff;box-shadow:0 4px 6px rgba(0,0,0,.15)}
.card h3{height:24px;background:linear-gradient(180deg,#6b6b6b,#4a4a4a);border-left:3px solid var(--accent);color:#fff;font-size:19px;padding-left:10px;line-height:26px;white-space:nowrap;overflow:hidden}
.card .pic{position:absolute;left:10px;top:31px;width:158px;height:74px}
.card p{position:absolute;left:10px;top:110px;width:162px;font-size:7.8px;line-height:12px}

/* testimonials */
.avatar{top:813px;width:64px;height:64px;border-radius:50%;border:2px solid var(--accent);background:linear-gradient(180deg,#d6dbe2,#7b8594)}
.quote{top:815px;width:205px;font-style:italic;font-size:7.4px;line-height:14px;color:#555;text-indent:38px}
.qmark{font:700 30px "Lato",sans-serif;color:#a9cfe6;top:803px}
.tline{top:888px;width:275px;height:1px;background:#ccc}
.name{top:898px;font:600 8px "Raleway",sans-serif;color:var(--accent)}
.dots{left:661px;top:924px;display:flex;gap:3px}
.dots span{width:5px;height:5px;border-radius:50%;background:#ccc}
.dots span:first-child{background:var(--accent)}

/* footer */
.foot-h{top:1027px;font-size:16px;color:#fff;border-bottom:1px solid rgba(255,255,255,.35);padding-bottom:3px;white-space:nowrap}
.links{left:106px;top:1054px;list-style:none;color:#fff;font-size:8px}
.links li{height:22.4px}
.links li::before{content:"• "}
.links li.on{font-weight:700}
.contact{left:224px;top:1054px;color:#fff;font-size:8px;line-height:11px}
.contact b{display:block;font-size:7.5px}
.contact .row{display:flex;align-items:center;gap:6px;margin-top:10px}
.map{left:389px;top:1056px;width:164px;height:99px;border:2px solid #fff;background:linear-gradient(135deg,#ece9e1,#dcd8cc)}
.follow{left:603px;top:1049px;color:#fff}
.follow .item{display:flex;align-items:center;gap:10px;height:36px}
.follow .dot{width:20px;height:20px;border-radius:50%;background:#1c4f86}
.follow .dot.tw{background:#27a2d0}
.follow .lbl{font-size:8px;line-height:8px}
.follow .lbl small{display:block;font-size:5.5px}
.bottom{left:0;top:1175px;width:794px;height:25px;background:var(--blue-bar);color:#fff;font-size:7.5px;text-align:center;line-height:25px}
</style>
</head>
<body>

<div class="abs hero" role="img" aria-label="Photograph of a timber-clad two-storey house among birch trees"></div>
<div class="abs topbar">
  <div class="abs social"><span></span><span></span><span></span></div>
  <div class="abs phone">
    <svg width="12" height="12" viewBox="0 0 24 24"><path fill="#fff" d="M6.6 10.8a15 15 0 0 0 6.6 6.6l2.2-2.2c.3-.3.7-.4 1-.2 1.1.4 2.3.6 3.6.6.6 0 1 .4 1 1V20c0 .6-.4 1-1 1A17 17 0 0 1 3 4c0-.6.4-1 1-1h3.5c.6 0 1 .4 1 1 0 1.3.2 2.5.6 3.6.1.3 0 .7-.2 1z"/></svg>
    (555) 214-3390
  </div>
</div>
<div class="abs header">
  <div class="abs logo"><i></i>Brenwick Structures</div>
  <ul class="abs nav">
    <li class="active">Home</li><li>Portfolio</li><li>Product Specs</li><li>Testimonials</li><li>Our Process</li><li>Contact Us</li>
  </ul>
</div>
<div class="abs arrow" style="left:56px"></div>
<div class="abs arrow" style="left:718px"></div>
<div class="abs caption script">Building Dreams, So You Can Build Memories</div>

<h2 class="abs heading script" style="top:406px">Welcome to <em>Brenwick Structures</em></h2>
<div class="abs rule" style="top:440px"></div>
<p class="abs intro">Lorem ipsum dolor sit amet, consectetuer adipiscing elit, sed diam nonummy nibh euismod tincidunt ut laoreet dolore magna aliquam erat volutpat. Ut wisi enim ad minim veniam, quis nostrud exerci tation ullamcorper suscipit lobortis nisl ut aliquip ex ea commodo consequat. Duis autem vel eum iriure dolor in hendrerit in vulputate velit esse molestie consequat, vel illum dolore eu feugiat nulla facilisis at vero eros et aexerci tation ullamcorper suscipit lobortis nisl ut aliquip ex ea commodo consequat. Duis autem vel eum iriure dolor in hendrerit in vulputate velit esse molestie .</p>

<div class="abs band"></div>
<div class="abs card" style="left:107px">
  <h3 class="script">Portfolio</h3>
  <div class="pic" role="img" aria-label="Photo of a single-storey timber cabin" style="background:linear-gradient(180deg,#8fb6de,#b07a46 60%,#5f7f3a)"></div>
  <p>Lorem ipsum dolor sit amet, consecte euismod tin dolore te feugait nulla facilisi.</p>
</div>
<div class="abs card" style="left:308px">
  <h3 class="script">Our Product</h3>
  <div class="pic" role="img" aria-label="Photo of a blue-sided family home" style="background:linear-gradient(180deg,#c7d3e0,#4d5f78 55%,#8b8f96)"></div>
  <p>Praesent luptatum zzrilconsecte euismod tin dolore te feugait nulla facilisi.</p>
</div>
<div class="abs card" style="left:509px">
  <h3 class="script">What We Do</h3>
  <div class="pic" role="img" aria-label="Video still of a green house with stone chimney" style="background:linear-gradient(180deg,#3d4a3a,#6d7a5a 55%,#9aa67a)"></div>
  <p>Nonummy nibh euismod tin ipsum dolor si nonummy nibh euismod nulla facilisi.</p>
</div>

<h2 class="abs heading script" style="top:752px">Client <em>Testimonials</em></h2>
<div class="abs rule" style="top:785px"></div>

<div class="abs avatar" style="left:107px" role="img" aria-label="Portrait of client"></div>
<div class="abs qmark" style="left:189px">&ldquo;</div>
<p class="abs quote" style="left:181px">Lorem ipsum dolor sit amet, consectet uer adipiscing elit, sed diam nonummy nibh euis mod tincidun nt ut laoreetml dolore magna aliquam erat volutpat. Ut wisi enim ad minim veniam, quis nostrud exer.</p>
<div class="abs tline" style="left:106px"></div>
<div class="abs name" style="left:230px">- Mr Corvan Elly</div>

<div class="abs avatar" style="left:412px" role="img" aria-label="Portrait of client"></div>
<div class="abs qmark" style="left:495px">&ldquo;</div>
<p class="abs quote" style="left:488px">Lorem ipsum dolor sit amet, consectet uer adipiscing elit, sed diam nonummy nibh euis mod tincidun nt ut laoreetml dolore magna aliquam erat volutpat. Ut wisi enim ad minim veniam, quis nostrud exer.</p>
<div class="abs tline" style="left:411px"></div>
<div class="abs name" style="left:527px">- Miss Talia Wrenfield</div>
<div class="abs dots"><span></span><span></span><span></span></div>

<svg class="abs" style="left:0;top:930px" width="794" height="270" viewBox="0 0 794 270">
  <defs><linearGradient id="sea" x1="0" y1="0" x2="0" y2="1"><stop offset="0" stop-color="#45aee0"/><stop offset="1" stop-color="#2a93c9"/></linearGradient></defs>
  <path d="M105,17 C300,0 520,75 794,50 L794,75 C520,100 300,30 105,17Z" fill="#c6c6c6"/>
  <path d="M0,22 C180,5 360,40 520,75 C640,95 730,85 794,75 L794,270 L0,270Z" fill="url(#sea)"/>
</svg>

<div class="abs foot-h script" style="left:106px;width:70px">Quick Links</div>
<ul class="abs links"><li class="on">Home</li><li>About us</li><li>Gallery</li><li>Clients</li><li>Contact us</li></ul>

<div class="abs foot-h script" style="left:224px;width:115px">Contact Information</div>
<div class="abs contact">
  <b>ASHCOMBE HOMES</b>Lorem ipsum dolor sit amet,<br>uis mml dolore magna
  <div class="row"><svg width="8" height="8" viewBox="0 0 24 24"><path fill="#fff" d="M6.6 10.8a15 15 0 0 0 6.6 6.6l2.2-2.2c.3-.3.7-.4 1-.2 1.1.4 2.3.6 3.6.6.6 0 1 .4 1 1V20c0 .6-.4 1-1 1A17 17 0 0 1 3 4c0-.6.4-1 1-1h3.5c.6 0 1 .4 1 1 0 1.3.2 2.5.6 3.6.1.3 0 .7-.2 1z"/></svg>555. 214. 3390</div>
  <div class="row"><svg width="8" height="8" viewBox="0 0 10 10"><rect x="2" y="0" width="6" height="3" fill="#fff"/><rect x="0" y="3.5" width="10" height="4" fill="#fff"/><rect x="2" y="7" width="6" height="3" fill="#fff"/></svg>555. 214. 3391</div>
  <div class="row"><svg width="8" height="6" viewBox="0 0 10 7"><rect width="10" height="7" fill="#fff"/><path d="M0,0 L5,4 L10,0" stroke="#2e9fd3" fill="none"/></svg>info@brenwickstructures.example</div>
</div>

<div class="abs foot-h script" style="left:389px;width:164px">Quick Contact</div>
<div class="abs map" role="img" aria-label="Street map showing the office location"></div>

<div class="abs foot-h script" style="left:603px;width:84px">Follow Us</div>
<div class="abs follow">
  <div class="item"><span class="dot"></span><span class="lbl">FRIENDWALL<small>BECOME A FAN</small></span></div>
  <div class="item"><span class="dot"></span><span class="lbl">WORKROUND<small>JOIN US ON</small></span></div>
  <div class="item"><span class="dot tw"></span><span class="lbl">CHIRPLINE<small>JOIN US ON</small></span></div>
</div>

<div class="abs bottom">© 2015 Brenwick Structures. All Rights Reserved.</div>
</body>
</html>
```